Self-Serve Brazilian Buffet and BBQ sold by the pound needs a business card

For CEO -Lucia Fernanda Matos Hale
Owner/President - Marcos Tiago Matos

Target Market(s)

Customers and

Industry/Entity Type

Business

Contact Information for Business Card

Lucia Fernanda Pinto Matos Hale
CEO of Vento Lume Grill
Brazilian BBQ Buffet sold by the pound

Requirements
Must have
• 5186 West Linden Blvd.
• Ste. K
• Santa Ana, CA 92704
• Phone : 555810-2947
• ventolumegrill@postrova.com

```html
<!DOCTYPE html>
<html lang="en">
<head>
<meta charset="utf-8">
<title>Vento Lume Grill — Business Card</title>
<link rel="stylesheet" href="https://fonts.googleapis.com/css2?family=Great+Vibes&family=Raleway:wght@300;400&display=swap">
<style>
  :root {
    --card-bg: #e2d1ae;
    --ink-dark: #1c1a18;
    --ink-soft: #3b3935;
    --rule: #2a2825;
  }
  html, body {
    margin: 0;
    padding: 0;
    width: 1200px;
    height: 800px;
    overflow: hidden;
    background: var(--card-bg);
  }
  .business-card {
    position: relative;
    width: 1200px;
    height: 800px;
    background: var(--card-bg);
    font-family: "Raleway", sans-serif;
    font-weight: 300;
    color: var(--ink-soft);
  }
  .brand-mark {
    position: absolute;
    left: 0;
    width: 1200px;
    top: 285px;
    display: flex;
    justify-content: center;
    align-items: center;
    gap: 14px;
  }
  .brand-mark__dot {
    width: 16px;
    height: 16px;
    border-radius: 50%;
    background: var(--ink-dark);
  }
  .brand-mark__name {
    font-family: "Raleway", sans-serif;
    font-weight: 400;
    font-size: 34px;
    letter-spacing: 3px;
    color: var(--ink-dark);
  }
  .holder-name {
    position: absolute;
    left: 0;
    width: 1200px;
    top: 382px;
    margin: 0;
    text-align: center;
    font-family: "Great Vibes", cursive;
    font-weight: 400;
    font-size: 78px;
    line-height: 1;
    color: var(--ink-dark);
  }
  .name-rule {
    position: absolute;
    left: 288px;
    top: 493px;
    width: 624px;
    height: 1px;
    background: var(--rule);
  }
  .holder-title {
    position: absolute;
    left: 0;
    width: 1200px;
    top: 520px;
    margin: 0;
    text-align: center;
    font-size: 40px;
    font-weight: 300;
    letter-spacing: 2px;
    color: var(--ink-soft);
  }
  .contact {
    position: absolute;
    margin: 0;
    font-size: 31px;
    font-weight: 300;
    line-height: 1.12;
    letter-spacing: 0.5px;
    color: var(--ink-soft);
  }
  .contact--phone { left: 42px; top: 662px; }
  .contact--email { left: 42px; top: 732px; }
  .contact--address {
    right: 30px;
    top: 664px;
    text-align: right;
    font-style: normal;
  }
</style>
</head>
<body>
  <main class="business-card">
    <div class="brand-mark">
      <span class="brand-mark__dot"></span>
      <span class="brand-mark__name">Vento Lume Grill</span>
    </div>

    <h1 class="holder-name">Lucia Fernanda Matos Hale</h1>
    <div class="name-rule"></div>
    <p class="holder-title">CEO</p>

    <p class="contact contact--phone">555810-2947</p>
    <p class="contact contact--email">ventolumegrill@postrova.com</p>

    <address class="contact contact--address">
      5186 West Linden Blvd.<br>
      Ste. K<br>
      Santa Ana, CA 92704
    </address>
  </main>
</body>
</html>
```